Larkspur Realty

Business cards for 4 people

They need to say for all
57 Danner Quay, Boston MA 02117

Each person will have their own personal information
We would like gold embossing for the name of the company
Mabel is the blonde sitting in the chair smiling her information should be on the back of the card with her name and information
Should say for slogan classic pattern, elevated experience
mabel@larkspurhomesnet.com
(413) 555-0182

Odessa is the brunette with wavy hair in the tan suit odessa@larkspurhomesnet.com
(617) 555-0147

june@larkspurhomesnet.com
(413) 555-0169
standing next to the chair

ruth@larkspurhomesnet.com
(413) 555-0193
close up headshot

```html
<!DOCTYPE html>
<html lang="en">
<head>
<meta charset="utf-8">
<title>Larkspur Realty – Business Card</title>
<link rel="stylesheet" href="https://fonts.googleapis.com/css2?family=Poppins:wght@400;500;600&display=swap">
<style>
  :root {
    --backdrop: #d4d4d4;
    --navy: #233452;
    --gold: #d2a93a;
    --white: #ffffff;
    --ink: #1f2a44;
    --photo-light: #c9c9cb;
    --photo-dark: #8f9096;
  }
  * { margin: 0; padding: 0; box-sizing: border-box; }
  html, body {
    width: 900px; height: 1200px; overflow: hidden;
    background: var(--backdrop);
    font-family: "Poppins", sans-serif;
  }
  .card {
    position: absolute;
    left: 135px; width: 630px;
    border-radius: 12px;
  }
  .card-front {
    top: 215px; height: 357px;
    background: var(--navy);
  }
  .brand-ring {
    position: absolute;
    left: 253px; top: 85px;
    width: 124px; height: 124px;
    border: 3px solid var(--gold);
    border-radius: 50%;
  }
  .brand-name {
    position: absolute;
    left: 0; right: 0; top: 222px;
    text-align: center;
    color: var(--gold);
    font-weight: 500;
    font-size: 30px;
    letter-spacing: 2px;
    text-transform: uppercase;
  }
  .card-back {
    top: 628px; height: 359px;
    background: var(--white);
  }
  .portrait {
    position: absolute;
    left: 41px; top: 60px;
    width: 242px; height: 242px;
    border-radius: 50%;
    border: 3px solid var(--navy);
    background: radial-gradient(circle at 50% 40%, var(--photo-light) 0%, var(--photo-light) 45%, var(--photo-dark) 100%);
  }
  .details {
    position: absolute;
    left: 324px; top: 55px;
    color: var(--ink);
  }
  .person-name {
    font-size: 24px; font-weight: 600; line-height: 1.2;
  }
  .slogan {
    font-size: 14px; font-weight: 400; margin-top: 2px;
  }
  .address {
    font-size: 15px; line-height: 23px; margin-top: 56px;
    letter-spacing: 0.4px;
  }
  .contacts {
    list-style: none;
    margin-top: 26px;
    font-size: 15px; line-height: 24.5px;
    letter-spacing: 0.3px;
  }
  .contacts li { display: flex; align-items: center; gap: 4px; }
  .contacts svg { width: 12px; height: 12px; fill: var(--ink); flex: none; }
</style>
</head>
<body>
  <section class="card card-front">
    <div class="brand-ring"></div>
    <div class="brand-name">Larkspur Realty</div>
  </section>

  <section class="card card-back">
    <div class="portrait" role="img" aria-label="Portrait photo of Mabel seated on a wooden chair, smiling"></div>
    <div class="details">
      <h1 class="person-name">Mabel Ashcombe</h1>
      <p class="slogan">Elevated Experience</p>
      <p class="address">57 Danner Quay,<br>Boston MA 02117</p>
      <ul class="contacts">
        <li>
          <svg viewBox="0 0 24 24" aria-hidden="true"><path d="M6.6 10.8a15.1 15.1 0 0 0 6.6 6.6l2.2-2.2a1 1 0 0 1 1-.25 11.4 11.4 0 0 0 3.6.57 1 1 0 0 1 1 1V20a1 1 0 0 1-1 1A17 17 0 0 1 3 4a1 1 0 0 1 1-1h3.5a1 1 0 0 1 1 1c0 1.25.2 2.45.57 3.57a1 1 0 0 1-.25 1z"/></svg>
          (413) 555-0182
        </li>
        <li>
          <svg viewBox="0 0 24 24" aria-hidden="true"><path d="M2 5h20v14H2z M2 5l10 8 10-8" /><path d="M2 6.5l10 7.5 10-7.5V19H2z" fill="#1f2a44"/></svg>
          mabel@larkspurhomesnet.com
        </li>
        <li>
          <svg viewBox="0 0 24 24" aria-hidden="true"><path d="M12 2a10 10 0 1 0 0 20 10 10 0 0 0 0-20zm6.9 6h-2.9a15.6 15.6 0 0 0-1.4-3.6A8 8 0 0 1 18.9 8zM12 4c.8 1.2 1.5 2.5 1.9 4h-3.8c.4-1.5 1.1-2.8 1.9-4zM4.3 14a8 8 0 0 1 0-4h3.4a16.5 16.5 0 0 0 0 4zm.8 2h2.9c.3 1.3.8 2.5 1.4 3.6A8 8 0 0 1 5.1 16zM8 8H5.1a8 8 0 0 1 4.3-3.6C8.8 5.5 8.4 6.7 8 8zm4 12c-.8-1.2-1.5-2.5-1.9-4h3.8c-.4 1.5-1.1 2.8-1.9 4zm2.3-6H9.7a14.7 14.7 0 0 1 0-4h4.6a14.7 14.7 0 0 1 0 4zm.3 5.6c.6-1.1 1.1-2.3 1.4-3.6h2.9a8 8 0 0 1-4.3 3.6zm1.7-5.6a16.5 16.5 0 0 0 0-4h3.4a8 8 0 0 1 0 4z"/></svg>
          www.larkspurhomesnet.com
        </li>
      </ul>
    </div>
  </section>
</body>
</html>
```